Chicago Train Advertisement for HomeAlongRail.com.

We have purchased one month of advertising on the Chicago NRX subway train. We will have 150 cards up in the subway to advertise our website HomeAlongRail.com where people can search for properties by train station. The cards are 11" tall and 46.5" long. We want people to feel compelled to jump on their cell phones and conduct a search for an apartment or home while they are riding the train, or at least enter their email and search criteria so one of our agents can help them.

Target Market(s)

People who want to live near train stations

Industry/Entity Type

Real Estate

Font styles to use
Sans Serif

Colors

Designer to choose colors to be used in the design.

Requirements
Must have
• The homealongrail logo and a catchy slogan, something like: Find your home near a train station the easy way: www.homealongral.com. Search real estate listings near the NRX or Velco.

```html
<!DOCTYPE html>
<html lang="en">
<head>
<meta charset="utf-8">
<title>HomeAlongRail.com – Train Card</title>
<link rel="stylesheet" href="https://fonts.googleapis.com/css2?family=Montserrat:wght@400;500;600&display=swap">
<style>
  :root {
    --backdrop: #5f5f5f;
    --card-white: #ffffff;
    --card-edge: #2b2b2b;
    --navy: #1c1640;
    --sky-blue: #4a9fdc;
    --body-gray: #555555;
    --rail-yellow: #eee53e;
    --photo-sky: #6f9bd4;
    --photo-house: #bfb0a8;
    --photo-shade: #9c9096;
    --photo-green: #4f8a34;
  }
  * { box-sizing: border-box; margin: 0; padding: 0; }
  html, body {
    width: 1200px;
    height: 568px;
    overflow: hidden;
    background: var(--backdrop);
    font-family: "Montserrat", sans-serif;
  }
  .train-card {
    position: absolute;
    left: 101px;
    top: 160px;
    width: 994px;
    height: 234px;
    background: var(--card-white);
    border: 1px solid var(--card-edge);
    overflow: hidden;
  }
  .rail-art {
    position: absolute;
    inset: 0;
    width: 100%;
    height: 100%;
  }
  .brand {
    position: absolute;
    left: 56px;
    top: 46px;
    display: flex;
    align-items: center;
    gap: 7px;
    color: var(--navy);
    font-weight: 600;
    font-size: 17px;
    letter-spacing: -0.2px;
  }
  .brand-dot {
    width: 14px;
    height: 14px;
    border-radius: 50%;
    background: var(--sky-blue);
  }
  .slogan {
    position: absolute;
    left: 56px;
    top: 94px;
    color: var(--sky-blue);
    font-weight: 500;
    font-size: 18px;
    line-height: 23px;
  }
  .web-address {
    position: absolute;
    left: 55px;
    top: 143px;
    color: var(--navy);
    font-weight: 500;
    font-size: 32px;
    letter-spacing: -0.3px;
  }
  .tagline {
    position: absolute;
    left: 56px;
    top: 187px;
    color: var(--body-gray);
    font-weight: 400;
    font-size: 14.5px;
  }
  .partner {
    position: absolute;
    left: 459px;
    top: 189px;
    display: flex;
    align-items: center;
    gap: 5px;
    color: var(--sky-blue);
    font-weight: 500;
    font-size: 12.5px;
  }
  .partner-dot {
    width: 12px;
    height: 12px;
    border-radius: 50%;
    background: var(--sky-blue);
  }
</style>
</head>
<body>
  <section class="train-card">
    <svg class="rail-art" viewBox="0 0 994 234" preserveAspectRatio="none" aria-hidden="false">
      <defs>
        <linearGradient id="streetscape-tones" x1="0" y1="0" x2="0" y2="1">
          <stop offset="0" stop-color="var(--photo-sky)"/>
          <stop offset="0.3" stop-color="#8fabcf"/>
          <stop offset="0.55" stop-color="var(--photo-house)"/>
          <stop offset="0.85" stop-color="var(--photo-shade)"/>
          <stop offset="1" stop-color="var(--photo-green)"/>
        </linearGradient>
      </defs>
      <polygon class="rail-stripe" points="329,0 343,0 800,234 727,234" fill="var(--rail-yellow)"/>
      <polygon class="rail-stripe" points="349,0 359,0 963,234 852,234" fill="var(--rail-yellow)"/>
      <polygon class="street-photo" role="img" aria-label="Photo of a row of Victorian houses under a blue sky with trees and shrubs"
               points="366,0 994,0 994,234 978,234" fill="url(#streetscape-tones)"/>
    </svg>

    <div class="brand"><span class="brand-dot"></span>HomeAlongRail.com</div>

    <p class="slogan">Find your home near a<br>Train station the easy way</p>
    <p class="web-address">www.homealongral.com</p>
    <p class="tagline">Search real estate listings near the NRX or Velco.</p>

    <div class="partner"><span class="partner-dot"></span>Kestrel Realty</div>
  </section>
</body>
</html>
```